Brasko Construction Business Card

I need a business card design for my company.
We are a construction/machinery company.
I would like to see my logo on the front of the card and my details on the other side
I would like the card to be black or dark grey in colour,with my logo as i send it or modified with a lighter blue colour
I would like to see the design kept fairly simple,but eye catching at the same time
Industry/Entity Type
Business
Contact Information for Business Card
Name
Phone Number
Address
Email
Colors
00a990
1b1b1b
000000
474747
ececec

```html
<!DOCTYPE html>
<html lang="en">
<head>
<meta charset="UTF-8">
<title>Brasko Construction Business Card</title>
<link href="https://fonts.googleapis.com/css2?family=Archivo:wght@400;600;800&display=swap" rel="stylesheet">
<style>
  :root {
    --backdrop: #3a3330;
    --card: #1b1b1b;
    --card-edge: #000000;
    --mark-grey: #9a9a9a;
    --text-light: #ececec;
    --text-muted: #bdbdbd;
    --divider: #474747;
  }
  html, body {
    margin: 0;
    padding: 0;
    width: 1200px;
    height: 814px;
    overflow: hidden;
    background: var(--backdrop);
    font-family: "Archivo", Arial, sans-serif;
  }
  .sheet {
    position: relative;
    width: 1200px;
    height: 814px;
    display: flex;
    align-items: center;
    justify-content: center;
    gap: 40px;
  }
  .card {
    width: 540px;
    height: 309px;
    background: var(--card);
    border: 1px solid var(--card-edge);
    box-sizing: border-box;
    position: relative;
  }
  .card-front {
    display: flex;
    align-items: center;
    justify-content: center;
  }
  .front-wordmark {
    display: flex;
    align-items: center;
    gap: 14px;
    color: var(--mark-grey);
    font-weight: 800;
    font-size: 34px;
    letter-spacing: 1px;
    text-transform: uppercase;
  }
  .front-wordmark .mark-square {
    width: 26px;
    height: 26px;
    background: var(--mark-grey);
  }
  .card-back {
    display: flex;
    align-items: center;
  }
  .back-brand {
    width: 270px;
    display: flex;
    align-items: center;
    justify-content: center;
  }
  .back-wordmark {
    color: var(--text-light);
    font-weight: 800;
    font-size: 24px;
    line-height: 1.1;
    text-transform: uppercase;
    letter-spacing: 1px;
    text-align: left;
  }
  .back-divider {
    width: 1px;
    height: 140px;
    background: var(--divider);
  }
  .contact {
    padding-left: 26px;
    color: var(--text-light);
  }
  .contact-name {
    font-weight: 800;
    font-size: 18px;
    margin: 0;
  }
  .contact-role {
    font-size: 13px;
    color: var(--text-muted);
    margin: 2px 0 14px;
  }
  .contact-address {
    font-size: 13px;
    line-height: 1.45;
    margin: 0 0 8px;
    font-style: normal;
  }
  .contact-line {
    display: flex;
    align-items: center;
    gap: 8px;
    font-size: 13px;
    line-height: 1.6;
  }
  .contact-line svg {
    width: 12px;
    height: 12px;
    fill: var(--text-light);
  }
</style>
</head>
<body>
<main class="sheet">
  <section class="card card-front" aria-label="Card front">
    <div class="front-wordmark">
      <span class="mark-square"></span>
      <span>Brasko Construction</span>
    </div>
  </section>

  <section class="card card-back" aria-label="Card back">
    <div class="back-brand">
      <div class="back-wordmark">Brasko<br>Construction</div>
    </div>
    <div class="back-divider"></div>
    <div class="contact">
      <p class="contact-name">Daniel Reyes</p>
      <p class="contact-role">CEO/Founder</p>
      <address class="contact-address">4120 Kelso Ridge Road<br>Fairbanks, Alaska 99701</address>
      <div class="contact-line">
        <svg viewBox="0 0 24 24" aria-hidden="true"><path d="M6.6 10.8a15.1 15.1 0 0 0 6.6 6.6l2.2-2.2a1 1 0 0 1 1-.25 11.4 11.4 0 0 0 3.6.57 1 1 0 0 1 1 1V20a1 1 0 0 1-1 1A17 17 0 0 1 3 4a1 1 0 0 1 1-1h3.5a1 1 0 0 1 1 1c0 1.25.2 2.45.57 3.6a1 1 0 0 1-.25 1z"/></svg>
        <span>555 218 4096</span>
      </div>
      <div class="contact-line">
        <svg viewBox="0 0 24 24" aria-hidden="true"><path d="M2 5h20v14H2z M4 7v.5l8 5 8-5V7l-8 5z" fill-rule="evenodd"/></svg>
        <span>hello@braskobuild.com</span>
      </div>
    </div>
  </section>
</main>
</body>
</html>
```